Stonelynk Business Card Design

The Stonelynk Co is an aggregate (crushing) equipment dealer serving Western Canadian provinces. Stonelynk is a distributor of aggregate equipment for different manufacturers.

We are looking to change and update the existing business card which has been used since the existence of the company. A copy of existing card has been attached for reference. The Stonelynk Co logo we want to remain the same and we want the green color to remain the same.

We are wanting something new with a different look. A refreshing card to show a new modern and updated look. No longer wanting to have the manufacturers on the back of the card but something more like our logo on the back of the card with a statement like "Crushing Solutions"

ideas could be:
- card can be different colors on front and back
- front or reverse of the card could possibly be the green color with the logo in black

Target Market(s)

Owners of Aggregate/Crushing companies

Requirements
Must have
• - logo to remain same along with same font within logo
• - green color to remain same
Nice to have
• as noted above under project description
Should not have

```html
<!DOCTYPE html>
<html lang="en">
<head>
<meta charset="UTF-8">
<title>The Stonelynk Co — Business Card</title>
<link rel="stylesheet" href="https://fonts.googleapis.com/css2?family=Oswald:wght@400;500;600;700&display=swap">
<style>
  :root {
    --brand-green: #777920;
    --accent-green: #8f8d26;
    --card-black: #0b0b0b;
    --ink-black: #0a0a0a;
    --text-white: #f2f2f2;
    --page-bg: #e9e6e0;
  }
  * { margin: 0; padding: 0; box-sizing: border-box; }
  html, body {
    width: 1200px;
    height: 800px;
    overflow: hidden;
  }
  body {
    background: var(--page-bg);
    font-family: "Oswald", "Arial Narrow", sans-serif;
    position: relative;
  }
  .card {
    position: absolute;
    top: 251px;
    width: 520px;
    height: 297px;
    box-shadow: 0 10px 28px rgba(0, 0, 0, 0.18);
  }

  /* Front: green with company name */
  .card--front {
    left: 60px;
    background: var(--brand-green);
    display: flex;
    flex-direction: column;
    align-items: center;
    justify-content: center;
    gap: 34px;
  }
  .front-mark {
    width: 96px;
    height: 96px;
    border-radius: 50%;
    background: var(--ink-black);
  }
  .front-name {
    color: var(--ink-black);
    font-weight: 700;
    font-size: 30px;
    letter-spacing: 0.5px;
    text-transform: uppercase;
  }

  /* Back: black with contact details */
  .card--back {
    left: 620px;
    background: var(--card-black);
    color: var(--text-white);
  }
  .back-mark {
    position: absolute;
    left: 28px;
    top: 30px;
    width: 42px;
    height: 42px;
    background: var(--accent-green);
  }
  .company-name {
    position: absolute;
    right: 26px;
    top: 44px;
    font-weight: 700;
    font-size: 30px;
    letter-spacing: 0.6px;
    line-height: 1;
    text-transform: uppercase;
  }
  .company-tagline {
    position: absolute;
    right: 26px;
    top: 84px;
    color: var(--accent-green);
    font-weight: 400;
    font-size: 14px;
    letter-spacing: 0.3px;
    line-height: 1;
  }
  .person {
    position: absolute;
    left: 28px;
    top: 110px;
  }
  .person-name {
    color: var(--accent-green);
    font-weight: 700;
    font-size: 21px;
    line-height: 1.05;
    text-transform: uppercase;
  }
  .person-role {
    font-weight: 400;
    font-size: 12px;
    line-height: 1.3;
    text-transform: uppercase;
  }
  .divider {
    position: absolute;
    height: 1px;
    background: var(--text-white);
  }
  .divider--main { left: 28px; right: 26px; top: 166px; }
  .divider--address { left: 300px; right: 26px; top: 230px; }
  .contact {
    position: absolute;
    font-weight: 400;
    font-size: 12px;
    line-height: 1.4;
    text-transform: uppercase;
    letter-spacing: 0.2px;
    white-space: nowrap;
  }
  .contact--online { left: 28px; top: 184px; }
  .contact--phone { left: 172px; top: 212px; }
  .contact--direct { right: 26px; top: 200px; text-align: right; }
  .contact--address { right: 26px; top: 244px; text-align: right; }
</style>
</head>
<body>

  <section class="card card--front" aria-label="Card front">
    <div class="front-mark"></div>
    <div class="front-name">The Stonelynk Co.</div>
  </section>

  <section class="card card--back" aria-label="Card back">
    <div class="back-mark"></div>
    <div class="company-name">The Stonelynk Co.</div>
    <div class="company-tagline">SCREENERS | CRUSHERS | STACKERS</div>

    <div class="person">
      <div class="person-name">Dale Morrow</div>
      <div class="person-role">Director</div>
    </div>

    <div class="divider divider--main"></div>

    <div class="contact contact--online">
      dale@stonelynk.com<br>
      www.stonelynk.ca
    </div>
    <div class="contact contact--phone">
      Tel : 780.555.0142<br>
      Fax : 780.555.0187
    </div>
    <div class="contact contact--direct">Direct : 780.555.0163</div>

    <div class="divider divider--address"></div>

    <div class="contact contact--address">
      2218 48B Avenue<br>
      Ridgeford, Alberta T4R 1K6
    </div>
  </section>

</body>
</html>
```